Create the BEST and COOLEST website for events and media company!

Hi there. I am a start-up events and conferences company with a twist, and we are seeking a highly modern website for our company Lumen Harbor Media. Our company believes that (like the social networking theory) that each and every one of us is connected to anyone on the planet in six connections or less. E.g. I know someone, who knows someone, who knows someone. Hence, the name Lumen Harbor Media.

I have included the copy for the website attached.

While we do have a business audience, they are in the fields of technology from the banking, health, government sector. We would like our website to be edgy, fresh and steer away from stuffy corporate images.

To give you an idea, our website menu tabs will be labelled:
HOME: This will include a corporate video that’s being created next week for me. However, please still design this page with a very striking background image that fills the whole page. You can run the copy and put a mock video for me to just see the layout (we can insert the finished video later).

ROCKSTARS: this will show pictures of highly powerful leaders speaking on stage; with a highly engaged audience watching. We want to show we have the world’s best technology International speakers “rockstars” who are the best in their game when it comes to talking about the future of technology.

LOCAL LEGENDS: like the international ‘rockstar’ speakers we would bring over to Australia to present; this LOCAL LEGENDS page should show we have the best home-grown Chief business people speaking at conferences and smaller powerful roundtable luncheons.

UNSUNG HEROES: this is more the people in the audience who ask questions on a microphone; those that attend the conferences; or a speaking to people at a conference.

THE BAND: this is like an ‘about us’ – just a funkier name to tie in with the theme of rockstars, etc.

THE PARTNERS: this is like a sponsor client page, where we invite people to partner with us and sponsor our events and conferences.

YOU & DORIAN FLECK: Dorian Fleck is a famous actor who made the term ‘six degrees of separation’ very popular. This page will have a little bit of an introduction, but mainly have the following video fill the landing page: https://www.vidstreamhub.example/watch?v=Qzt-plK4WB8

Website Functionality and Features:

• Try and make the ‘vibe’ and look and feel consistent, hip and modern (but still maintain a professional look). At the end of the day, people looking at our website are very senior business chiefs of organisations and also marketing chiefs.
• We may add more pages once we become established, so the website needs to ensure we can do that easily.
• We want pictures to not look stock photos. We want them to fresh, innovative, inspirational.
• Images should have a ‘wow’ factor. Like this one: https://www.stockframebank.example/detail/news-photo/general-view-of-crowd-during-brightloop-talks-2018-news-photo/481203967
• Need a mix of speaker, stage, audience, pictures. While we want to be fresh, edgy and contemporary we need to remember our viewers are the big chiefs of businesses – so lets try and have cool shots, but ensure there is a link to the business decision makers in a modern way. They all don’t have to wear suits, but not too casual either
• Other types of imagery I like is this one: https://www.stockframebank.example/detail/photo/smiling-audience-using-smart-phone-flashlights-for-royalty-free-image/372815094.
• The following are ok, not wow – but to give you an idea:
• https://www.stockframebank.example/detail/photo/smiling-male-speaker-in-wheelchair-on-stage-royalty-free-image/372816288
https://www.stockframebank.example/detail/photo/smiling-woman-with-camera-phone-in-dark-audience-royalty-free-image/372817452
https://www.stockframebank.example/detail/photo/audience-using-camera-phones-royalty-free-image/376630581
https://www.stockframebank.example/detail/photo/male-speaker-on-stage-talking-to-audience-royalty-free-image/372818736

NB: Logos are supplied in low resolution, but I can send you high resolution also
Updates

Hi there I will be adding two low-resolution images of my business partner and I for the ABOUT US page which is called THE BAND in the menu tab.

Hi everyone, thank you for your designs. I have uploaded a MAIN SCREEN IDEAS word document to give you further ideas of how the options I like for the main landing page on the home page. Hope this helps!

Target Market(s)

High end business people in marketing and business.

Coding

Coded - Design and coding required

Number of Pages Required

5+ page

Font styles to use
Sans Serif

Requirements
Must have
• Fresh, inspirational and aspirational designs. We need to make events and conferences look exciting and that we are bring the best technology speakers (like BrightLoop events) to our audience of marketing and technology professionals.
Should not have
• Cheesy, old stock photos; or pictures of American executives as this is for an Australian audience.
• PLEASE do not include an UPCOMING EVENTS or a SPEAKERS section as we will not be having this showcasing. You can feature ROCK STARS, LOCAL LEGENDS and UNSUNG HEROES if you like on the home page + the video of YOU and DORIAN FLECK (with his picture on the video box with a play button)

```html
<!DOCTYPE html>
<html lang="en">
<head>
<meta charset="utf-8">
<title>Lumen Harbor Media — Where Leaders Connect</title>
<link href="https://fonts.googleapis.com/css2?family=Montserrat:wght@300;400;600&display=swap" rel="stylesheet">
<style>
  :root {
    --white: #ffffff;
    --ink: #0f1114;
    --footer-bg: #15171b;
    --footer-text: #8d8f93;
    --hero-dark: #1f1a17;
    --hero-mid: #4a4038;
    --hero-cloth: #8e8a86;
    --tile-a: #3c3c3c;
    --tile-b: #5a5a5a;
    --tile-c: #2a2a2a;
    --tile-d: #1e1f21;
  }
  * { box-sizing: border-box; margin: 0; padding: 0; }
  html, body { width: 1200px; height: 658px; overflow: hidden; background: var(--ink); }
  body { font-family: "Montserrat", sans-serif; color: var(--white); position: relative; }

  .hero {
    position: absolute; left: 0; top: 0; width: 1200px; height: 504px;
    background:
      radial-gradient(ellipse 260px 200px at 620px 330px, rgba(142,138,134,0.55), transparent 70%),
      linear-gradient(90deg, #3b3632 0%, var(--hero-dark) 25%, var(--hero-mid) 55%, #3a342f 80%, #5c5854 100%);
  }
  .hero-shade { position: absolute; inset: 0; background: rgba(0,0,0,0.25); }

  .brand {
    position: absolute; left: 44px; top: 58px;
    display: flex; align-items: center; gap: 10px;
  }
  .brand-dot { width: 14px; height: 14px; border-radius: 50%; background: var(--white); }
  .brand-name { font-size: 18px; font-weight: 400; letter-spacing: 2.5px; color: var(--white); }

  .menu-toggle { position: absolute; left: 1119px; top: 56px; width: 38px; height: 27px; }
  .menu-toggle span { position: absolute; left: 0; width: 38px; height: 3px; background: var(--white); }
  .menu-toggle span:nth-child(1) { top: 0; }
  .menu-toggle span:nth-child(2) { top: 12px; }
  .menu-toggle span:nth-child(3) { top: 24px; }

  .slide-arrow { position: absolute; top: 320px; width: 32px; height: 20px; }
  .slide-arrow.prev { left: 6px; opacity: 0.6; }
  .slide-arrow.next { left: 1163px; }

  .hero-title {
    position: absolute; left: 0; width: 1200px; top: 274px;
    text-align: center; font-size: 34px; font-weight: 600; letter-spacing: 1px;
    padding-left: 30px;
  }
  .play-button { position: absolute; left: 595px; top: 331px; width: 76px; height: 76px; }

  .sections { position: absolute; left: 0; top: 504px; width: 1200px; height: 129px; display: flex; }
  .section-tile {
    width: 300px; height: 129px; position: relative;
    display: flex; align-items: center; justify-content: center;
  }
  .section-tile .photo { position: absolute; inset: 0; }
  .section-tile .label {
    position: relative; font-size: 19px; font-weight: 300; letter-spacing: 0.3px; color: var(--white);
  }
  .section-tile.is-active .label { font-weight: 600; }
  .rock-stars .photo { background: linear-gradient(135deg, var(--tile-b), var(--tile-a) 60%, #4a4a4a); }
  .local-legends .photo { background: linear-gradient(90deg, #6d6d6d, var(--tile-a) 40%, #7a7a7a 70%, #9a9a9a); }
  .unsung-heroes .photo { background: linear-gradient(135deg, var(--tile-c), #505050 60%, #6a6a6a); }
  .you-and-dorian .photo { background: linear-gradient(90deg, var(--tile-d) 40%, #3a3a3a 70%, var(--tile-d)); }

  .site-footer {
    position: absolute; left: 0; top: 633px; width: 1200px; height: 25px;
    background: var(--footer-bg); color: var(--footer-text);
    font-size: 11.5px; text-align: center; line-height: 25px; letter-spacing: 0.2px;
  }
</style>
</head>
<body>
  <header class="hero">
    <div class="hero-shade" role="img" aria-label="Executives seated along a long dining table at a roundtable luncheon in a dark wood-panelled private room"></div>

    <div class="brand">
      <span class="brand-dot"></span>
      <span class="brand-name">LUMEN HARBOR MEDIA</span>
    </div>

    <div class="menu-toggle" aria-label="Menu"><span></span><span></span><span></span></div>

    <svg class="slide-arrow prev" viewBox="0 0 32 20" aria-label="Previous slide">
      <path d="M31 10H3M11 2L3 10l8 8" fill="none" stroke="#fff" stroke-width="2.5"/>
    </svg>
    <svg class="slide-arrow next" viewBox="0 0 32 20" aria-label="Next slide">
      <path d="M1 10h28M21 2l8 8-8 8" fill="none" stroke="#fff" stroke-width="2.5"/>
    </svg>

    <h1 class="hero-title">WHERE LEADERS CONNECT</h1>

    <svg class="play-button" viewBox="0 0 76 76" aria-label="Play video">
      <circle cx="38" cy="38" r="37" fill="rgba(255,255,255,0.18)"/>
      <circle cx="38" cy="38" r="26" fill="#fff"/>
      <path d="M33 29v18l14-9z" fill="#111"/>
    </svg>
  </header>

  <nav class="sections">
    <a class="section-tile rock-stars">
      <div class="photo" role="img" aria-label="Black and white shot of an excited conference audience"></div>
      <span class="label">ROCK STARS</span>
    </a>
    <a class="section-tile local-legends is-active">
      <div class="photo" role="img" aria-label="Black and white shot of a roundtable luncheon"></div>
      <span class="label">LOCAL LEGENDS</span>
    </a>
    <a class="section-tile unsung-heroes">
      <div class="photo" role="img" aria-label="Black and white shot of an attendee asking a question in the audience"></div>
      <span class="label">UNSUNG HEROES</span>
    </a>
    <a class="section-tile you-and-dorian">
      <div class="photo" role="img" aria-label="Black and white portrait of the actor Dorian Fleck"></div>
      <span class="label">YOU &amp; DORIAN FLECK</span>
    </a>
  </nav>

  <footer class="site-footer">Copyright © 2019 LUMEN HARBOR MEDIA. All Rights Reserved.</footer>
</body>
</html>
```